Harborline Pension Group Needs a Fresh Business Card Update!

We are looking forward to a busy year ahead and have just launched our new website. We are looking to you for a fresh update to our business cards!

Here is a link to our website: http://www.harborlinepensiongrp.com/

You will find our logo attached in two formats for your use. Our old business card front and back is also attached for your reference. We want to have a portrait space on the new cards similar to the old card that we can interchange with various employee portraits or keep blank.
We are also interested in seeing a play on colors that matches our website and logo.

For the back of the card please make the following changes (from our old card):

1. The new "FREE REPORT" is titled as follows: FREE REPORT - Six Pitfalls That Drain Nest Eggs

2. Under "How Can We Help You?" please list out the following in place of the longer list:

Determine Retirement Eligibility & Best Date for You to Retire
Organizing Important Documents for Retirement
Calculate your annuity estimate
Completing Retirement Paperwork
Survivor Benefit Options
Deposits and Re-deposits
Military Service
Social Security Questions
CAPD Special Supplement
Health Insurance
Early-Out Options
Meadow Reserve Fund (during service and after retirement)

3. Under: "Am I on Track to Retire?" please edit the sentence to read:
Find out by Scheduling a "FREE" Federal Benefit & Analysis Counseling Session

Designers, Thank you for your creativity!

Target Market(s)

Federal Employees ages 45-65

Industry/Entity Type

Financial Planning

Contact Information for Business Card

We want to have a portrait space on the front of the new cards similar to the old card that we can interchange with various employee portraits or keep blank. The only text that is negotiable on the front of the card is the bulleted text.
We would like for you to use colors that match our website and logo.

Survivor Benefit Options
Deposits and Re-deposits
Military Service
Social Security Questions
CAPD Special Supplement
Health Insurance
Early-Out Options

Font styles to use
Serif

Requirements
Must have
• Colors to match our logo and new website: http://www.harborlinepensiongrp.com/

```html
<!DOCTYPE html>
<html lang="en">
<head>
<meta charset="utf-8">
<title>Harborline Pension Group – Business Card</title>
<link href="https://fonts.googleapis.com/css2?family=Cinzel:wght@400;600;700&family=Arimo:wght@400;700&display=swap" rel="stylesheet">
<style>
  :root{
    --navy:#0f1c33;
    --navy-deep:#0b1528;
    --blue:#1d8ad0;
    --blue-bright:#2f9be0;
    --red:#c1222e;
    --white:#ffffff;
    --paper:#ececec;
    --grey:#8c9096;
  }
  *{box-sizing:border-box;margin:0;padding:0}
  html,body{width:1200px;height:900px;overflow:hidden}
  body{background:var(--paper);font-family:"Arimo",Arial,sans-serif;position:relative}

  .card{position:absolute;left:250px;width:700px;height:400px;background:var(--navy);overflow:hidden;box-shadow:0 6px 18px rgba(0,0,0,.25)}
  .card--back{top:28px}
  .card--front{top:472px}

  /* back */
  .report-band{position:absolute;left:0;top:0;width:100%;height:76px;background:var(--blue);color:var(--white);padding:16px 0 0 250px}
  .report-title{font-family:"Cinzel",serif;font-size:18px;font-weight:600;letter-spacing:.5px}
  .report-title span{font-family:"Arimo",sans-serif;font-weight:400;font-size:16px;letter-spacing:0}
  .report-url{font-size:13px;margin-top:5px;padding-left:120px}
  .help-band{position:absolute;left:0;top:76px;width:100%;height:34px;background:var(--white);text-align:right;padding:8px 34px 0 0}
  .help-title{font-family:"Cinzel",serif;font-weight:700;color:var(--red);font-size:18px;letter-spacing:.5px}
  .cover{position:absolute;left:48px;top:96px;width:160px;height:210px;background:linear-gradient(160deg,#d22a2a,#9e1b1b);box-shadow:3px 4px 8px rgba(0,0,0,.5)}
  .services{position:absolute;right:30px;top:122px;text-align:right;list-style:none;color:var(--white);font-size:13.5px;line-height:19px}
  .bullet{display:inline-block;width:7px;height:7px;background:var(--blue-bright);margin:0 4px 1px 6px}
  .track-title{position:absolute;right:34px;top:286px;font-family:"Cinzel",serif;font-weight:700;color:var(--red);font-size:19px;letter-spacing:.5px}
  .session{position:absolute;left:36px;bottom:26px;color:var(--white);font-size:17px}
  .session em{font-style:normal;color:var(--blue-bright)}

  /* front */
  .portrait{position:absolute;left:462px;top:18px;width:196px;height:214px;background:linear-gradient(180deg,#9a9ea4,#4b4f56)}
  .rule{position:absolute;left:150px;top:234px;width:550px;height:2px;background:var(--red)}
  .brand{position:absolute;left:36px;top:176px;display:flex;align-items:center;gap:10px;max-width:410px}
  .brand-mark{width:42px;height:42px;border-radius:50%;border:2px solid var(--white);flex:none}
  .brand-name{font-family:"Cinzel",serif;font-weight:600;font-size:20px;color:var(--blue-bright);letter-spacing:.3px;white-space:nowrap}
  .person{position:absolute;right:30px;top:244px;text-align:right}
  .person-name{font-family:"Cinzel",serif;font-weight:700;color:var(--blue-bright);font-size:27px;letter-spacing:1px}
  .taglines{list-style:none;color:var(--white);font-size:14px;line-height:18px;margin-top:4px}
  .address{position:absolute;left:36px;top:244px;color:var(--blue-bright);font-size:15px}
  .contacts{position:absolute;left:36px;top:268px;list-style:none;color:var(--white);font-size:15px;line-height:19px}
  .contacts li{display:flex;align-items:center;gap:8px}
  .contacts svg{width:12px;height:12px;flex:none}
  .contacts .site{color:var(--blue-bright)}
  .contacts .site b{font-weight:400;color:var(--white)}
  .dedication{position:absolute;left:36px;bottom:12px;color:var(--white);font-size:13px;font-variant:small-caps;letter-spacing:.3px}
</style>
</head>
<body>

<section class="card card--back" aria-label="Card back">
  <header class="report-band">
    <p class="report-title">FREE REPORT <span>– Six Pitfalls That Drain Nest Eggs</span></p>
    <p class="report-url">www.harborlinepensiongrp.com</p>
  </header>
  <div class="help-band"><h2 class="help-title">HOW CAN WE HELP YOU?</h2></div>
  <div class="cover" role="img" aria-label="Cover of the book The Prepared Saver by Daniel Merrow"></div>
  <ul class="services">
    <li>Determine Retirement Eligibility &amp; Best Date for You to Retire<i class="bullet"></i></li>
    <li>Organizing Important Documents for Retirement<i class="bullet"></i></li>
    <li>Calculate your annuity estimate<i class="bullet"></i></li>
    <li>Completing Retirement Paperwork<i class="bullet"></i></li>
    <li>Survivor Benefit Options<i class="bullet"></i>Deposits and Re-deposits<i class="bullet"></i></li>
    <li>Military Service<i class="bullet"></i>Social Security Questions<i class="bullet"></i></li>
    <li>CAPD Special Supplement<i class="bullet"></i>Health Insurance<i class="bullet"></i>Early-Out Options<i class="bullet"></i></li>
    <li>Meadow Reserve Fund (during service and after retirement)<i class="bullet"></i></li>
  </ul>
  <h2 class="track-title">AM I ON TRACK TO RETIRE?</h2>
  <p class="session">Find out by Scheduling a "<em>FREE</em>" Federal Benefit &amp; Analysis Counseling Session</p>
</section>

<section class="card card--front" aria-label="Card front">
  <div class="portrait" role="img" aria-label="Employee portrait space"></div>
  <div class="brand">
    <span class="brand-mark"></span>
    <span class="brand-name">Harborline Pension Group</span>
  </div>
  <div class="rule"></div>
  <div class="person">
    <h1 class="person-name">DANIEL MERROW</h1>
    <ul class="taglines">
      <li>Information You Need<i class="bullet"></i></li>
      <li>Advice You Can Trust<i class="bullet"></i></li>
      <li>Support You Can Count On<i class="bullet"></i></li>
    </ul>
  </div>
  <p class="address">Alder Ave., Suite 210 Brookfield, CO 80412</p>
  <ul class="contacts">
    <li><svg viewBox="0 0 12 12"><path d="M2 1l2 0 1 3-1.5 1a7 7 0 0 0 3.5 3.5L8 7l3 1v2a1 1 0 0 1-1 1A9 9 0 0 1 1 2a1 1 0 0 1 1-1z" fill="#c1222e"/></svg>720-555-0148</li>
    <li><svg viewBox="0 0 12 12"><path d="M2 1l2 0 1 3-1.5 1a7 7 0 0 0 3.5 3.5L8 7l3 1v2a1 1 0 0 1-1 1A9 9 0 0 1 1 2a1 1 0 0 1 1-1z" fill="#c1222e"/></svg>1-877-555-0192 (Toll Free)</li>
    <li><svg viewBox="0 0 12 12"><rect x="1" y="2" width="10" height="8" rx="1" fill="#c1222e"/><rect x="3" y="4" width="6" height="4" fill="#0f1c33"/></svg>1-888-555-0137</li>
    <li><svg viewBox="0 0 12 12"><rect x="1" y="2.5" width="10" height="7" fill="none" stroke="#c1222e" stroke-width="1.4"/><path d="M1 3l5 4 5-4" fill="none" stroke="#c1222e" stroke-width="1.2"/></svg>daniel@danielmerrow.com</li>
    <li><svg viewBox="0 0 12 12"><circle cx="6" cy="6" r="5" fill="none" stroke="#c1222e" stroke-width="1.4"/><path d="M1 6h10M6 1c-3 3-3 7 0 10M6 1c3 3 3 7 0 10" fill="none" stroke="#c1222e" stroke-width="1"/></svg><span class="site"><b>www.</b>harborlinepensiongrp<b>.com</b></span></li>
  </ul>
  <p class="dedication">Dedicated to and Specializing in CSRS/CAPD &amp; the Financial Needs of Federal Employees</p>
</section>

</body>
</html>
```